Silver Brook Custom Homes business card. Double sided. Modern. professional

Silver Brook Custom Homes
contemporary modern design with our logo /
Double sided with all our contact information
Use same Green colors as in our Logo. Contemporary logo that grabs your attention. Visually pleasing and balanced. Easy to read, and Vibrant. Would love an option for rounded edges. Embossed logo would be amazing.
Contact Information for Business Card
Dana Pellman Owner / General Contractor Silver Brook Custom Homes p: 803.555.0142 m: 865.555.0178 e: silverbrookcustomhomes@mailnest.example w: www.silverbrookcustomhomes.example 218 Wrenfield Mill Road Batesburg, SC 29088

```html
<!DOCTYPE html>
<html lang="en">
<head>
<meta charset="utf-8">
<title>Silver Brook Custom Homes – Business Card</title>
<link href="https://fonts.googleapis.com/css2?family=Roboto:wght@400;500;700&display=swap" rel="stylesheet">
<style>
  :root {
    --stage: #3f3f3f;
    --card-white: #f2f2f2;
    --card-black: #121212;
    --brand-green: #6b8a2e;
    --ink: #1e1e1e;
    --emboss: #1f1f1f;
  }
  * { margin: 0; padding: 0; box-sizing: border-box; }
  html, body { width: 1200px; height: 810px; overflow: hidden; }
  body {
    background: var(--stage);
    font-family: "Roboto", Arial, sans-serif;
    display: flex; flex-direction: column; align-items: center; justify-content: center;
    gap: 50px;
  }
  .card {
    width: 560px; height: 320px;
    border-radius: 22px;
    position: relative;
    overflow: hidden;
  }
  .card--front { background: var(--card-white); display: flex; align-items: center; }
  .card--back { background: var(--card-black); display: flex; align-items: center; justify-content: center; }

  .brand { width: 262px; display: flex; align-items: center; justify-content: center; gap: 10px; }
  .brand__dot { width: 14px; height: 14px; border-radius: 50%; background: var(--brand-green); flex: none; }
  .brand__name {
    font-weight: 500; color: var(--brand-green);
    font-size: 19px; letter-spacing: 2px; line-height: 1.25; text-transform: uppercase;
  }
  .divider { width: 2px; height: 160px; background: var(--brand-green); flex: none; }

  .contact { padding-left: 22px; color: var(--ink); }
  .contact__name { font-weight: 700; color: var(--brand-green); font-size: 22px; text-transform: uppercase; letter-spacing: -0.3px; line-height: 1; }
  .contact__title { font-weight: 500; font-size: 11px; text-transform: uppercase; margin-top: 3px; }
  .contact__address { font-size: 11.5px; line-height: 1.35; margin-top: 14px; }
  .contact__list { list-style: none; margin-top: 10px; }
  .contact__item { display: flex; align-items: center; gap: 8px; font-size: 11.5px; line-height: 1.55; }
  .contact__icon { width: 12px; height: 12px; flex: none; }

  .back-brand { display: flex; align-items: center; gap: 14px; }
  .back-brand__dot { width: 20px; height: 20px; border-radius: 50%; background: var(--emboss); }
  .back-brand__name { font-weight: 500; color: var(--emboss); font-size: 30px; letter-spacing: 4px; line-height: 1.2; text-transform: uppercase; }
</style>
</head>
<body>
  <section class="card card--front">
    <div class="brand">
      <span class="brand__dot"></span>
      <div class="brand__name">Silver Brook<br>Custom Homes</div>
    </div>
    <div class="divider"></div>
    <div class="contact">
      <div class="contact__name">Dana Pellman</div>
      <div class="contact__title">Owner</div>
      <div class="contact__address">218 Wrenfield Mill Road<br>Batesburg, SC 29088</div>
      <ul class="contact__list">
        <li class="contact__item">
          <svg class="contact__icon" viewBox="0 0 24 24"><path fill="#6b8a2e" d="M6.6 10.8a15 15 0 0 0 6.6 6.6l2.2-2.2a1 1 0 0 1 1-.25 11 11 0 0 0 3.6.6 1 1 0 0 1 1 1V20a1 1 0 0 1-1 1A17 17 0 0 1 3 4a1 1 0 0 1 1-1h3.5a1 1 0 0 1 1 1 11 11 0 0 0 .6 3.6 1 1 0 0 1-.25 1z"/></svg>
          803.555.0142
        </li>
        <li class="contact__item">
          <svg class="contact__icon" viewBox="0 0 24 24"><rect x="6" y="2" width="12" height="20" rx="2" fill="#6b8a2e"/><rect x="8" y="5" width="8" height="11" fill="#f2f2f2"/><circle cx="12" cy="19" r="1.2" fill="#f2f2f2"/></svg>
          865.555.0178
        </li>
        <li class="contact__item">
          <svg class="contact__icon" viewBox="0 0 24 24"><rect x="2" y="5" width="20" height="14" rx="1.5" fill="#6b8a2e"/><path d="M3 6l9 7 9-7" fill="none" stroke="#f2f2f2" stroke-width="1.6"/></svg>
          silverbrookcustomhomes@mailnest.example
        </li>
        <li class="contact__item">
          <svg class="contact__icon" viewBox="0 0 24 24"><g fill="none" stroke="#6b8a2e" stroke-width="2"><circle cx="12" cy="12" r="9.5"/><ellipse cx="12" cy="12" rx="4" ry="9.5"/><path d="M2.5 12h19M4 7h16M4 17h16"/></g></svg>
          www.silverbrookcustomhomes.example
        </li>
      </ul>
    </div>
  </section>

  <section class="card card--back">
    <div class="back-brand">
      <span class="back-brand__dot"></span>
      <div class="back-brand__name">Silver Brook<br>Custom Homes</div>
    </div>
  </section>
</body>
</html>
```